Seeking Talented PSD Designer for Real Estate Finance Web Site

Hello ...
Need a minimalist design for a high - end finance web site that conveys prestige / sophistication / class ... Below are comps for this project ...
http://www.copperlanefunding.com/
http://mirowayfunding.com/
http://www.tolvinedgp.com/
http://quillanfunding.com/
Look forward too receiving proposals for this project ....
Target Market(s)
Commerciale entities seeking more than $500.0 k in interim capital ... These could include apartment owners / construction managers / restaurant owners / hotels / golf courses ...
Industry/Entity Type
Real Estate
Number of Pages Required
1 page
Requirements
Must have
- Super high quality graphic design ... Has to be marketable and convert customers to contact us ...
- Please refer to logo concept four ....
Should not have
- clunky / poor fonts /

```html
<!DOCTYPE html>
<html lang="en">
<head>
<meta charset="utf-8">
<title>Halvorsen Capital</title>
<link rel="stylesheet" href="https://fonts.googleapis.com/css2?family=Raleway:wght@400;500&family=Open+Sans:wght@400;600&display=swap">
<style>
  :root {
    --navy: #2f4269;
    --navy-deep: #2c3e63;
    --white: #ffffff;
    --ink: #1d1d1f;
    --muted: #6b6b6b;
    --photo-top: #44464f;
    --photo-bottom: #5b5556;
    --logo-grey: #8a8a8a;
  }
  * { margin: 0; padding: 0; box-sizing: border-box; }
  html, body { width: 1200px; height: 1127px; overflow: hidden; background: var(--white); }
  body { position: relative; font-family: "Open Sans", sans-serif; }

  .brand-block {
    position: absolute; left: 0; top: 0; width: 436px; height: 198px;
    background: var(--white);
    display: flex; align-items: center; justify-content: center; gap: 14px;
  }
  .brand-mark { width: 44px; height: 44px; border-radius: 50%; background: var(--navy); }
  .brand-name {
    font-family: "Raleway", sans-serif; font-weight: 400; font-size: 30px;
    letter-spacing: 5px; color: var(--navy); line-height: 1.1;
  }

  .hero-photo {
    position: absolute; left: 436px; top: 0; width: 764px; height: 805px;
    background: linear-gradient(180deg, var(--photo-top) 0%, #4a4a52 55%, var(--photo-bottom) 100%);
  }

  .main-nav {
    position: absolute; left: 437px; top: 0; width: 706px; height: 84px;
    border-bottom: 1px solid rgba(255,255,255,0.85);
  }
  .main-nav a {
    position: absolute; top: 42px; font-size: 13px; color: var(--white);
    text-decoration: none; white-space: nowrap;
  }
  .main-nav a.is-active::after {
    content: ""; position: absolute; left: -14px; right: -14px; top: 33px;
    height: 4px; background: var(--white);
  }

  .hero-panel {
    position: absolute; left: 0; top: 198px; width: 436px; height: 607px;
    background: var(--navy); color: var(--white);
  }
  .hero-title {
    position: absolute; left: 45px; top: 48px;
    font-family: "Raleway", sans-serif; font-weight: 500; font-size: 53px;
    line-height: 67px; letter-spacing: -0.5px;
  }
  .hero-text { position: absolute; left: 47px; font-size: 15.5px; line-height: 28px; width: 370px; }
  .hero-text.intro { top: 294px; }
  .hero-sub { position: absolute; left: 47px; top: 380px; font-size: 17px; text-transform: uppercase; }
  .hero-text.detail { top: 436px; }

  .welcome { position: absolute; left: 0; top: 805px; width: 1200px; height: 235px; text-align: center; }
  .welcome-title {
    position: absolute; left: 0; width: 1200px; top: 36px;
    font-family: "Raleway", sans-serif; font-weight: 500; font-size: 35px; color: var(--ink);
    padding-left: 44px;
  }
  .welcome-title span { color: var(--navy); }
  .welcome-rule { position: absolute; left: 491px; top: 91px; width: 126px; height: 3px; background: var(--navy); }
  .welcome-text {
    position: absolute; left: 135px; top: 106px; width: 880px;
    font-size: 12.3px; line-height: 28px; color: var(--muted);
  }

  .site-footer { position: absolute; left: 0; top: 1040px; width: 1200px; height: 87px; background: var(--navy-deep); }
  .copyright {
    position: absolute; left: 0; width: 1200px; top: 41px; text-align: center;
    font-size: 10.5px; font-weight: 600; color: var(--white); padding-left: 0;
  }
  .social { position: absolute; right: 66px; top: 43px; display: flex; gap: 28px; }
  .social span { width: 12px; height: 12px; border-radius: 50%; background: #c9ced8; display: block; }
</style>
</head>
<body>
  <header class="brand-block">
    <div class="brand-mark"></div>
    <div class="brand-name">HALVORSEN<br>CAPITAL</div>
  </header>

  <div class="hero-photo" role="img" aria-label="Dimmed photograph of a glass office tower rising behind an older concrete building"></div>

  <nav class="main-nav">
    <a class="is-active" href="#" style="left:25px">Home</a>
    <a href="#" style="left:108px">About Us</a>
    <a href="#" style="left:209px">Transactions</a>
    <a href="#" style="left:329px">Team</a>
    <a href="#" style="left:408px">Loan</a>
    <a href="#" style="left:484px">Contact</a>
  </nav>

  <section class="hero-panel">
    <h1 class="hero-title">WELCOME TO<br>HALVORSEN<br>CAPITAL</h1>
    <p class="hero-text intro">Lorem ipsum dolor sit amet, consectetur adipiscing elit, sed do tempor incididunt ut labore</p>
    <p class="hero-sub">Lorem ipsum dolor sit amet</p>
    <p class="hero-text detail">Lorem ipsum dolor sit amet, consectetur adipiscing elit, sed do eiusmod tempor incididunt ut labore et dolore minim veniam magna aliqua.</p>
  </section>

  <section class="welcome">
    <h2 class="welcome-title">Welcome to <span>HALVORSEN CAPITAL</span></h2>
    <div class="welcome-rule"></div>
    <p class="welcome-text">Lorem ipsum dolor sit amet, consectetur adipiscing elit, sed do eiusmod tempor incididunt ut labore et dolore magna aliqua. Ut enim ad minim veniam, quis nostrud exercitation ullamco laboris nisi ut aliquip ex ea commodo consequat. Duis aute irure dolor in reprehenderit in voluptate velit esse cillum dolore eu fugiat nulla pariatur. Excepteur sint occaecat cupidatat non proident, sunt in culpa qui officia deserunt mollit anim id est laborum.</p>
  </section>

  <footer class="site-footer">
    <p class="copyright">© All Rights Reserved. Copyrights @Halvorsen Capital. 2016</p>
    <div class="social" aria-label="Social links">
      <span></span><span></span><span></span><span></span><span></span>
    </div>
  </footer>
</body>
</html>
```